The Brightwater Compass Business Card

We need an attractive business card with the logo that we bought from ArtVantly last year.
Our mission is to contribute to change the way today's leaders manage business companies bringing value to the workplace and helping them to build a new model of creating wealth.
Our logo is clear about our values : we seek Positive Change through People and are convinced that the pursuit of individual well-being and the chase of economic results can converge with the right management.
Management Consulting
Corinne Fabrelle
+34 612 98 70 31
corinne.fabrelle@thebrightwatercompass-mail.net
www.thebrightwatercompass-mail.net

```html
<!DOCTYPE html>
<html lang="en">
<head>
<meta charset="utf-8">
<title>The Brightwater Compass – Business Card</title>
<link rel="stylesheet" href="https://fonts.googleapis.com/css2?family=Open+Sans:wght@400;600;700&display=swap">
<style>
  :root {
    --backdrop: #202020;
    --card-light: #dcecec;
    --card-light-edge: #e9f3f3;
    --teal: #68ab9d;
    --teal-deep: #4f9585;
    --teal-soft: #7dbcb0;
    --teal-ink: #3f8a7a;
    --white: #f2f8f7;
    --map-tint: rgba(120, 170, 165, 0.12);
  }
  * { box-sizing: border-box; margin: 0; padding: 0; }
  html, body {
    width: 1200px; height: 1200px; overflow: hidden;
    background: var(--backdrop);
    font-family: "Open Sans", Arial, sans-serif;
  }
  .sheet {
    width: 1200px; height: 1200px;
    display: flex; flex-direction: column; align-items: center; justify-content: center;
    gap: 50px;
  }
  .card {
    position: relative;
    width: 840px; height: 520px;
    overflow: hidden;
    box-shadow: 0 10px 30px rgba(0,0,0,0.5);
  }

  /* Contact side */
  .card--contact { background: var(--card-light); }
  .card--contact .map-tint {
    position: absolute; left: 0; top: 0; width: 100%; height: 44%;
    background: radial-gradient(ellipse at 60% 50%, var(--map-tint), transparent 70%);
  }
  .holder {
    position: absolute; left: 48px; top: 112px;
  }
  .holder__name {
    font-weight: 700; font-size: 38px; letter-spacing: 1px;
    font-variant: small-caps; color: var(--teal-ink);
  }
  .holder__role {
    font-size: 17px; letter-spacing: 1px; text-transform: uppercase;
    color: var(--teal-ink); margin-top: 2px; padding-left: 4px;
  }
  .brand {
    position: absolute; right: 52px; top: 96px;
    display: flex; flex-direction: column; align-items: center; gap: 14px;
  }
  .brand__dot {
    width: 70px; height: 70px; border-radius: 50%; background: var(--teal-ink);
  }
  .brand__name {
    font-weight: 600; font-size: 26px; color: var(--teal-ink); letter-spacing: 0.5px;
  }
  .contact-band {
    position: absolute; left: 0; top: 232px; width: 100%; height: 248px;
    background: linear-gradient(90deg, var(--teal-deep), var(--teal) 60%, var(--teal-soft));
  }
  .contact-band__rail {
    position: absolute; left: 40px; top: 0; bottom: 0; width: 3px; background: var(--white);
  }
  .contact-list { list-style: none; position: absolute; left: 22px; top: 34px; }
  .contact-list li {
    display: flex; align-items: center; gap: 18px; height: 62px;
    color: var(--white); font-size: 27px;
  }
  .contact-list .icon {
    width: 40px; height: 40px; border-radius: 50%;
    background: var(--white); display: flex; align-items: center; justify-content: center;
    flex: none;
  }

  /* Brand side */
  .card--brand {
    background: linear-gradient(135deg, var(--teal-deep), var(--teal) 45%, var(--teal-soft));
  }
  .card--brand .edge {
    position: absolute; left: 0; width: 100%; height: 22px; background: rgba(255,255,255,0.12);
  }
  .card--brand .edge--top { top: 0; }
  .card--brand .edge--bottom { bottom: 0; }
  .card--brand .map-tint {
    position: absolute; inset: 22px 0;
    background: radial-gradient(ellipse at 50% 50%, rgba(255,255,255,0.10), transparent 70%);
  }
  .brand-lockup {
    position: absolute; inset: 0;
    display: flex; flex-direction: column; align-items: center; justify-content: center; gap: 30px;
  }
  .brand-lockup__dot {
    width: 120px; height: 120px; border-radius: 50%; background: var(--white);
  }
  .brand-lockup__name {
    font-weight: 600; font-size: 50px; color: var(--white); letter-spacing: 1px;
  }
</style>
</head>
<body>
<main class="sheet">
  <section class="card card--contact">
    <div class="map-tint" role="img" aria-label="Faint world map background"></div>
    <div class="holder">
      <div class="holder__name">Corinne Fabrelle</div>
      <div class="holder__role">Designation</div>
    </div>
    <div class="brand">
      <div class="brand__dot"></div>
      <div class="brand__name">The Brightwater Compass</div>
    </div>
    <div class="contact-band">
      <div class="contact-band__rail"></div>
      <ul class="contact-list">
        <li>
          <span class="icon">
            <svg width="22" height="22" viewBox="0 0 24 24"><path fill="#4f9585" d="M6.6 10.8a15 15 0 0 0 6.6 6.6l2.2-2.2c.3-.3.7-.4 1-.2 1.1.4 2.3.6 3.6.6.6 0 1 .4 1 1V20c0 .6-.4 1-1 1A17 17 0 0 1 3 4c0-.6.4-1 1-1h3.5c.6 0 1 .4 1 1 0 1.3.2 2.5.6 3.6.1.3 0 .7-.2 1z"/></svg>
          </span>
          +34 612 98 70 31
        </li>
        <li>
          <span class="icon">
            <svg width="22" height="22" viewBox="0 0 24 24"><rect x="3" y="6" width="18" height="12" fill="none" stroke="#4f9585" stroke-width="2"/><path d="M3 6l9 7 9-7" fill="none" stroke="#4f9585" stroke-width="2"/></svg>
          </span>
          corinne.fabrelle@thebrightwatercompass-mail.net
        </li>
        <li>
          <span class="icon">
            <svg width="22" height="22" viewBox="0 0 24 24" fill="none" stroke="#4f9585" stroke-width="1.8"><circle cx="12" cy="12" r="9"/><ellipse cx="12" cy="12" rx="4" ry="9"/><path d="M3 12h18M5 7h14M5 17h14"/></svg>
          </span>
          www.thebrightwatercompass-mail.net
        </li>
      </ul>
    </div>
  </section>

  <section class="card card--brand">
    <div class="edge edge--top"></div>
    <div class="map-tint" role="img" aria-label="Faint world map background"></div>
    <div class="edge edge--bottom"></div>
    <div class="brand-lockup">
      <div class="brand-lockup__dot"></div>
      <div class="brand-lockup__name">The Brightwater Compass</div>
    </div>
  </section>
</main>
</body>
</html>
```